Redgum Wrecking P/L business card

I already have a EPS logo design that I wish to use however, the company is a demolition company based on the Central Coast of NSW Australia. The company is called "Redgum Wrecking P/L".

We offer demolition services such as Residential, Commercial, Civil, Asbestos removal, Excavation and Tree removal that are required to be displayed on the rear of the business card.

We currently have 4 personnel that require business cards with their specific contact details.

The logo is mid blue on a white background and the remainder is black text on a whiter card.

The eps logo supplied should only be displayed as a logo without the text.

Target Market(s)

People, governments, companies requiring demolition services on the east coast of NSW, specifically Central Coast, Sydney and Newcastle locations.

Industry/Entity Type

Business

Contact Information for Business Card

There are four cards required
First card:
Martin Ellory
Operations Director
Mobile No. 0451 872164
E: info@redgumwreck.example.com.au
www.redgumwreck.example.com.au
Second card:
Peter Hollis
Project Director
Company Mobile: 0451 872164
Personal Mobile: 0426 158 309
www.redgumwreck.example.com.au
Third card:
Simon Brady
Project Director
Company Mobile: 0451 872 164
Personal Mobile: 0433 917 482
www.redgumwreck.example.com.au
Fourth card:
Lewis Thornby
General Manager
Personal Mobile: 0447 261 835
www.redgumwreck.example.com.au

Font styles to use
Other font styles liked:
• Helvetica

Colors
33a6d7

Requirements
Must have
• The RW logo (without the text of Redgum Wrecking)
Horizontal layout with logo on top left hand corner
Services provision on the rear of the card
Nice to have
• Logo on top left corner
Text should be something like Helvetica
Should not have
• Do not include the text that is incorporated in the EPS file I sent ….just the logo

```html
<!DOCTYPE html>
<html lang="en">
<head>
<meta charset="utf-8">
<title>Redgum Wrecking – Business Card</title>
<link rel="stylesheet" href="https://fonts.googleapis.com/css2?family=Josefin+Sans:wght@400&family=Open+Sans:wght@400;700&display=swap">
<style>
  :root {
    --backdrop: #e4e2de;
    --card: #ffffff;
    --card-shade: #f1f1f1;
    --brand-teal: #2eaac3;
    --band-grey: #c6c7c9;
    --ink: #333333;
    --ink-soft: #444444;
  }
  * { margin: 0; padding: 0; box-sizing: border-box; }
  html, body {
    width: 1200px;
    height: 899px;
    overflow: hidden;
    background: var(--backdrop);
  }
  .card {
    position: absolute;
    left: 75px;
    top: 150px;
    width: 1050px;
    height: 600px;
    background: radial-gradient(circle at 45% 55%, var(--card) 0%, var(--card) 35%, var(--card-shade) 100%);
    box-shadow: 0 10px 30px rgba(0,0,0,0.18);
    overflow: hidden;
    font-family: "Open Sans", Arial, sans-serif;
  }
  .card__swoosh {
    position: absolute;
    inset: 0;
    width: 100%;
    height: 100%;
  }
  .brand {
    position: absolute;
    left: 70px;
    top: 70px;
    display: flex;
    align-items: center;
    gap: 14px;
  }
  .brand__dot {
    width: 22px;
    height: 22px;
    border-radius: 50%;
    background: var(--brand-teal);
  }
  .brand__name {
    font-family: "Josefin Sans", Arial, sans-serif;
    font-weight: 400;
    font-size: 44px;
    letter-spacing: 1px;
    color: var(--brand-teal);
    text-transform: uppercase;
  }
  .contact {
    position: absolute;
    left: 70px;
    top: 190px;
    list-style: none;
    color: var(--ink-soft);
    font-size: 20px;
    line-height: 30px;
  }
  .contact__item {
    display: flex;
    align-items: flex-start;
    gap: 10px;
  }
  .contact__icon {
    flex: none;
    width: 20px;
    height: 20px;
    margin-top: 5px;
  }
  .person {
    position: absolute;
    right: 150px;
    bottom: 40px;
    text-align: right;
    color: var(--ink);
  }
  .person__name {
    font-weight: 700;
    font-size: 42px;
    line-height: 52px;
  }
  .person__role {
    font-weight: 400;
    font-size: 38px;
    line-height: 48px;
  }
</style>
</head>
<body>
  <div class="card">
    <svg class="card__swoosh" viewBox="0 0 1050 600" aria-hidden="true">
      <path d="M560,0 Q920,190 975,600 L1050,600 L1050,0 Z" fill="var(--band-grey)"/>
      <path d="M690,0 Q960,170 1050,500 L1050,0 Z" fill="var(--brand-teal)"/>
      <path d="M880,200 Q1000,320 1040,540 Q990,350 880,200 Z" fill="var(--band-grey)"/>
    </svg>

    <div class="brand">
      <span class="brand__dot"></span>
      <span class="brand__name">Redgum Wrecking</span>
    </div>

    <ul class="contact">
      <li class="contact__item">
        <svg class="contact__icon" viewBox="0 0 20 20"><circle cx="10" cy="10" r="10" fill="var(--ink-soft)"/><path d="M5 10 L10 5 L15 10 L13.5 10 L13.5 15 L6.5 15 L6.5 10 Z" fill="#fff"/></svg>
        <span>Unit # 14, Kerr Bldg,<br>NSW 2250</span>
      </li>
      <li class="contact__item">
        <svg class="contact__icon" viewBox="0 0 20 20"><circle cx="10" cy="10" r="10" fill="var(--ink-soft)"/><path d="M6 5 L8.5 5 L9.5 8 L8 9 Q9 11.5 11 12 L12 10.5 L15 11.5 L15 14 Q9 15 6 8 Z" fill="#fff"/></svg>
        <span>0451 872 164</span>
      </li>
      <li class="contact__item">
        <svg class="contact__icon" viewBox="0 0 20 20"><circle cx="10" cy="10" r="10" fill="var(--ink-soft)"/><rect x="7" y="4" width="6" height="12" rx="1" fill="#fff"/><rect x="8" y="5.5" width="4" height="7" fill="var(--ink-soft)"/></svg>
        <span>0426 158 309</span>
      </li>
      <li class="contact__item">
        <svg class="contact__icon" viewBox="0 0 20 20"><circle cx="10" cy="10" r="10" fill="var(--ink-soft)"/><rect x="5" y="7" width="10" height="7" rx="1" fill="#fff"/><rect x="7" y="4" width="6" height="3" fill="#fff"/></svg>
        <span>0433 917 482</span>
      </li>
      <li class="contact__item">
        <svg class="contact__icon" viewBox="0 0 20 20"><circle cx="10" cy="10" r="10" fill="var(--ink-soft)"/><rect x="5" y="6.5" width="10" height="7" fill="#fff"/><path d="M5 6.5 L10 10.5 L15 6.5" stroke="var(--ink-soft)" stroke-width="1" fill="none"/></svg>
        <span>info@redgumwreck.example.com.au</span>
      </li>
      <li class="contact__item">
        <svg class="contact__icon" viewBox="0 0 20 20"><circle cx="10" cy="10" r="10" fill="var(--ink-soft)"/><circle cx="10" cy="10" r="5.5" stroke="#fff" stroke-width="1.2" fill="none"/><ellipse cx="10" cy="10" rx="2.3" ry="5.5" stroke="#fff" stroke-width="1.2" fill="none"/><line x1="4.5" y1="10" x2="15.5" y2="10" stroke="#fff" stroke-width="1.2"/></svg>
        <span>www.redgumwreck.example.com.au</span>
      </li>
    </ul>

    <div class="person">
      <p class="person__name">Owen Hartley</p>
      <p class="person__role">Owner / C.E.O</p>
    </div>
  </div>
</body>
</html>
```